Construction Company Stationary Design

We have previously utilised Artelvo to develop a new logo, we wanted to implement it for a while to ensure we liked it before rolling out new stationary. The time has come and we require:
Business Cards
"With Compliments" Cards
Asset Stickers
Vehicle Stickers
Letterhead
Document Header
Invoice Header
Cover Page
We are an established Construction Company working in Northern Australia (outback) that is venturing into a more corporate environment. We DO NOT do residential construction, we focus on commercial & government (Defence, schools, health etc) and work in both urban and remote environments.
Business Card Requirements:
• Logo
• Company Name
• Staff Name
• Staff Position
• Company Physical & Postal Address
• ABN
• Staff Mobile
• Staff Direct Phone (if applicable)
• Staff Email
• Office Phone
• Office Fax
"With Compliments" cards to be much the same as the business cards but with company details only (no staff details)
Asset stickers again to be much the same but with a space to write in asset number.
Document header requires 4 spaces to enter details much like our previous one attached.
We appreciate that designers time is valuable and would request that samples only be produced for one or two of the required items (say Business Card & Letterhead) and await a feedback score of 4 or more prior to producing the full suite of stationary.
If you require any further information please do not hesitate to contact me. colin@brevmark.com.au
Construction

```html
<!DOCTYPE html>
<html lang="en">
<head>
<meta charset="utf-8">
<title>Brevmark Constructions – Stationery Suite</title>
<link rel="stylesheet" href="https://fonts.googleapis.com/css2?family=Montserrat:wght@500;600;700&family=Open+Sans:wght@400;600;700&display=swap">
<style>
  :root {
    --bg: #d9d9d9;
    --paper: #f7f7f7;
    --ink: #3a3a3a;
    --muted: #666;
    --dark: #2b2b2b;
    --dark-2: #232323;
    --orange: #e4501f;
    --white: #ffffff;
  }
  * { box-sizing: border-box; margin: 0; padding: 0; }
  html, body { width: 1200px; height: 900px; overflow: hidden; }
  body {
    background: var(--bg);
    font-family: "Open Sans", Arial, sans-serif;
    color: var(--ink);
    position: relative;
  }
  .sheet { position: absolute; background: var(--paper); }
  .dark { background: var(--dark); color: var(--white); }

  /* brand name (wordmark stand-in) */
  .brand { display: flex; align-items: center; gap: 6px; }
  .brand-square { background: var(--orange); flex: none; }
  .brand-name {
    font-family: "Montserrat", Arial, sans-serif;
    font-weight: 700;
    color: var(--ink);
    line-height: 1.05;
    letter-spacing: 0.04em;
    text-transform: uppercase;
  }
  .dark .brand-name { color: var(--white); }

  /* letterhead */
  .letterhead { left: 220px; top: 54px; width: 382px; height: 540px; }
  .letterhead .brand { position: absolute; left: 38px; top: 34px; }
  .letterhead .brand-square { width: 14px; height: 14px; }
  .letterhead .brand-name { font-size: 12px; }
  .contact-list { position: absolute; left: 237px; top: 32px; font-size: 5.2px; line-height: 7px; }
  .contact-list li { list-style: none; display: flex; align-items: center; gap: 3px; }
  .contact-list li::before { content: ""; width: 4px; height: 4px; background: var(--orange); border-radius: 1px; }
  .postal { margin-top: 4px; }
  .letter { position: absolute; left: 58px; top: 108px; width: 310px; font-size: 5.4px; line-height: 7px; }
  .letter p { margin-bottom: 6px; text-align: justify; }
  .letter .date, .letter .recipient { margin-bottom: 30px; }
  .letter .date { margin-bottom: 9px; }
  .letter .salutation { font-weight: 700; margin-bottom: 8px; }
  .sign-off { display: flex; align-items: flex-end; gap: 12px; }
  .sign-off strong { display: block; font-weight: 700; }
  .signature { width: 76px; height: 32px; background: linear-gradient(90deg, #e9ecf5, #dfe4f3); border-radius: 2px; }
  .footer-band { position: absolute; left: 0; bottom: 0; width: 100%; height: 10px; display: block; }

  /* folder */
  .folder { left: 650px; top: 40px; width: 415px; height: 553px; border-radius: 4px; }
  .folder .spine { position: absolute; left: 28px; top: 0; bottom: 0; width: 1px; background: #3c3c3c; }
  .folder .brand { position: absolute; left: 0; right: 0; top: 120px; justify-content: center; gap: 10px; }
  .folder .brand-square { width: 24px; height: 24px; }
  .folder .brand-name { font-size: 22px; }

  /* business cards */
  .card { width: 164px; height: 91px; left: 78px; }
  .card-front { top: 638px; }
  .card-back { top: 748px; }
  .card-front .person { position: absolute; left: 11px; top: 12px; font-size: 5.6px; line-height: 7px; }
  .card-front .person strong { color: var(--orange); font-weight: 700; font-size: 6px; display: block; }
  .card-front .brand { position: absolute; right: 10px; top: 14px; gap: 4px; }
  .card-front .brand-square { width: 8px; height: 8px; }
  .card-front .brand-name { font-size: 7px; text-align: right; }
  .card-front .contact-list { left: 11px; top: 43px; font-size: 4.2px; line-height: 5.2px; }
  .card-front .abn { position: absolute; right: 10px; bottom: 14px; font-size: 4.2px; }
  .card-front .footer-band { height: 5px; }
  .card-back .brand { position: absolute; inset: 0; justify-content: center; gap: 6px; }
  .card-back .brand-square { width: 12px; height: 12px; }
  .card-back .brand-name { font-size: 10px; }

  /* compliments slip */
  .slip { left: 278px; top: 640px; width: 400px; height: 199px; }
  .slip .brand { position: absolute; left: 28px; top: 26px; gap: 7px; }
  .slip .brand-square { width: 14px; height: 14px; }
  .slip .brand-name { font-size: 13px; }
  .slip .postal { position: absolute; left: 26px; top: 168px; font-size: 5.4px; line-height: 7px; margin: 0; }
  .slip .footer-band { height: 9px; }

  /* envelope */
  .envelope { left: 724px; top: 640px; width: 400px; height: 199px; background: var(--paper); }
  .envelope .flap { position: absolute; left: 0; top: 0; width: 400px; height: 56px; display: block; }
  .envelope .brand { position: absolute; left: 0; right: 0; top: 26px; justify-content: center; gap: 4px; }
  .envelope .brand-square { width: 7px; height: 7px; }
  .envelope .brand-name { font-size: 7px; color: var(--white); }
</style>
</head>
<body>

<!-- Letterhead -->
<section class="sheet letterhead">
  <div class="brand"><span class="brand-square"></span><span class="brand-name">Brevmark<br>Constructions</span></div>
  <ul class="contact-list">
    <li>(08) 8900 4120</li>
    <li>(08) 8900 4121</li>
    <li>info@brevmark.com.au</li>
    <li>www.brevmark.com.au</li>
  </ul>
  <div class="contact-list postal" style="top:64px">PO Box 4410, Karrow NT 0822<br>18 Saltbush Rd, Karrow Flats</div>

  <article class="letter">
    <p class="date">30.02.2015</p>
    <p class="recipient">Recipient's name<br>Lindenweg 7<br>20095 Hamburg<br>Germany</p>
    <p class="salutation">Dear sir,</p>
    <p>Thank you for meeting with our team last week. We are pleased to confirm our interest in the project and look forward to working with you on the next stage of planning.</p>
    <p>Our crew has delivered commercial and government works across urban and remote sites for many years. We bring careful planning, safe practice and clear reporting to every job we take on, from early design through to final handover.</p>
    <p>Please find the attached schedule and cost summary for your review. Should any item need further detail, our project manager will gladly arrange a site visit at a time that suits you.</p>
    <p>We value your trust and hope to build a long working relationship with your organisation.</p>
    <div class="sign-off">
      <p>Yours Sincerely,<strong>Dana Keller</strong></p>
      <div class="signature" role="img" aria-label="Handwritten signature"></div>
    </div>
  </article>

  <svg class="footer-band" viewBox="0 0 382 10" preserveAspectRatio="none" aria-hidden="true">
    <rect width="382" height="10" fill="var(--dark)"/>
    <path d="M0 0 H238 C246 0 250 4 253 10 H0 Z" fill="var(--orange)"/>
  </svg>
</section>

<!-- Presentation folder -->
<section class="sheet dark folder">
  <span class="spine"></span>
  <div class="brand"><span class="brand-square"></span><span class="brand-name">Brevmark<br>Constructions</span></div>
</section>

<!-- Business card front -->
<section class="sheet card card-front">
  <div class="person"><strong>COLIN HARLOW</strong>Project Manager</div>
  <div class="brand"><span class="brand-square"></span><span class="brand-name">Brevmark<br>Constructions</span></div>
  <ul class="contact-list">
    <li>0400 118 245</li>
    <li>(08) 8900 4120</li>
    <li>(08) 8900 4121</li>
    <li>colin@brevmark.com.au</li>
    <li>www.brevmark.com.au</li>
  </ul>
  <div class="contact-list" style="left:11px;top:73px;font-size:4.2px;line-height:5.2px">PO Box 4410, Karrow NT 0822<br>18 Saltbush Rd, Karrow Flats</div>
  <span class="abn">ABN 12 345 678 901</span>
  <svg class="footer-band" viewBox="0 0 164 5" preserveAspectRatio="none" aria-hidden="true">
    <rect width="164" height="5" fill="var(--dark)"/>
    <path d="M0 0 H96 C100 0 102 2 104 5 H0 Z" fill="var(--orange)"/>
  </svg>
</section>

<!-- Business card back -->
<section class="sheet dark card card-back">
  <div class="brand"><span class="brand-square"></span><span class="brand-name">Brevmark<br>Constructions</span></div>
</section>

<!-- With compliments slip -->
<section class="sheet slip">
  <div class="brand"><span class="brand-square"></span><span class="brand-name">Brevmark<br>Constructions</span></div>
  <p class="postal">PO Box 4410, Karrow NT 0822<br>18 Saltbush Rd, Karrow Flats</p>
  <svg class="footer-band" viewBox="0 0 400 9" preserveAspectRatio="none" aria-hidden="true">
    <rect width="400" height="9" fill="var(--dark)"/>
    <path d="M0 0 H262 C268 0 271 4 274 9 H0 Z" fill="var(--orange)"/>
  </svg>
</section>

<!-- Envelope -->
<section class="sheet envelope">
  <svg class="flap" viewBox="0 0 400 56" preserveAspectRatio="none" aria-hidden="true">
    <path d="M0 0 H400 L390 56 H10 Z" fill="var(--dark)"/>
  </svg>
  <div class="brand"><span class="brand-square"></span><span class="brand-name">Brevmark</span></div>
</section>

</body>
</html>
```